Business Card Design Project - IT Company

Kestrafield Information Technology Solutions
We are an Information Technology Company. We provide computer services to commercial companies. We would like a new card full color front and back with bleeding edge.
We have a logo that you can use or if you want to come up with a new logo that is fine too.
Our colors are mostly Maroon and black but be creative.
Sample Information
Brent R Okafor
4812 W Saguaro Ridge Drive
Suite 600
Phoenix, AZ 85016
O: 602.914.2037
C: 602.468.1290
24/7: 888.914.2037
bokafor@kestrafield.example
www.kestrafield.example
Target Market(s)
Business of all sizes
Industry/Entity Type
Computer
Requirements
Must have
- Bleeding edge
full color on both sides

```html
<!DOCTYPE html>
<html lang="en">
<head>
<meta charset="utf-8">
<title>Kestrafield Business Card Options</title>
<link rel="stylesheet" href="https://fonts.googleapis.com/css2?family=Open+Sans:wght@400;600;700&display=swap">
<style>
  :root {
    --maroon: #c1272d;
    --slate: #636466;
    --paper: #ffffff;
    --ink: #58595b;
    --stage: #3b2219;
    --label: #ffffff;
  }
  * { margin: 0; padding: 0; box-sizing: border-box; }
  html, body { width: 1200px; height: 900px; overflow: hidden; }
  body {
    background: var(--stage);
    font-family: "Open Sans", Arial, sans-serif;
    position: relative;
  }
  .option-label {
    position: absolute;
    color: var(--label);
    font-size: 30px;
    font-weight: 400;
    font-family: Arial, "Open Sans", sans-serif;
    text-align: center;
  }
  .card {
    position: absolute;
    width: 580px;
    height: 334px;
    overflow: hidden;
  }
  .card--white { background: var(--paper); }
  .card--slate { background: var(--slate); }
  .card--maroon { background: var(--maroon); }
  .card__band {
    position: absolute;
    left: 0;
    bottom: 8px;
    width: 100%;
    height: 20px;
    display: block;
  }
  .card--front { left: 10px; top: 16px; }
  .card--back-one { left: 610px; top: 154px; }
  .card--back-two { left: 10px; top: 550px; }
  .card--back-three { left: 610px; top: 550px; }

  .holder-name {
    position: absolute;
    left: 30px;
    top: 78px;
    color: var(--maroon);
    font-size: 20px;
    font-weight: 700;
  }

  /* Company name placeholder: one font, one weight, one colour */
  .company {
    position: absolute;
    font-family: "Open Sans", Arial, sans-serif;
    font-weight: 600;
    text-align: center;
    line-height: 1.15;
  }
  .company__name { display: block; }
  .company__line { display: block; }

  .card--front .company { right: 24px; top: 46px; color: var(--ink); }
  .card--front .company__name { font-size: 28px; }
  .card--front .company__line { font-size: 11px; margin-top: 2px; }

  .company--centered { left: 0; right: 0; top: 132px; }
  .company--centered .company__name { font-size: 32px; }
  .company--centered .company__line { font-size: 12px; margin-top: 3px; }
  .company--light { color: var(--paper); }
  .company--dark { color: var(--ink); }

  .contact-address {
    position: absolute;
    left: 110px;
    top: 184px;
    font-size: 13.5px;
    color: var(--ink);
  }
  .contact-list {
    position: absolute;
    top: 214px;
    list-style: none;
    font-size: 13.5px;
    color: var(--ink);
    line-height: 20px;
  }
  .contact-list--phones { left: 110px; }
  .contact-list--web { left: 306px; }
  .contact-list__key { color: var(--maroon); font-weight: 700; }
</style>
</head>
<body>

  <section class="card card--white card--front" aria-label="Front side">
    <p class="holder-name">Brent R Okafor</p>
    <p class="company">
      <span class="company__name">Kestrafield</span>
      <span class="company__line">Information Technology Solutions</span>
    </p>
    <p class="contact-address">4812 W Saguaro Ridge Drive Suite 600, Phoenix, AZ 85016</p>
    <ul class="contact-list contact-list--phones">
      <li><span class="contact-list__key">O:</span> 602.914.2037</li>
      <li><span class="contact-list__key">C:</span> 602.468.1290</li>
      <li><span class="contact-list__key">24/7:</span> 888.914.2037</li>
    </ul>
    <ul class="contact-list contact-list--web">
      <li><span class="contact-list__key">E:</span> bokafor@kestrafield.example</li>
      <li>www.kestrafield.example</li>
    </ul>
    <svg class="card__band" viewBox="0 0 580 20" preserveAspectRatio="none" aria-hidden="true">
      <polygon points="0,0 434,0 428,20 0,20" fill="var(--maroon)"/>
      <polygon points="440,0 580,0 580,20 434,20" fill="var(--slate)"/>
    </svg>
  </section>
  <p class="option-label" style="left:10px; width:580px; top:356px;">Front side</p>

  <p class="option-label" style="left:610px; width:580px; top:106px;">Back side option 1</p>
  <section class="card card--slate card--back-one" aria-label="Back side option 1">
    <p class="company company--centered company--light">
      <span class="company__name">Kestrafield</span>
      <span class="company__line">Information Technology Solutions</span>
    </p>
    <svg class="card__band" viewBox="0 0 580 20" preserveAspectRatio="none" aria-hidden="true">
      <polygon points="0,0 434,0 428,20 0,20" fill="var(--paper)"/>
      <polygon points="440,0 580,0 580,20 434,20" fill="var(--maroon)"/>
    </svg>
  </section>

  <p class="option-label" style="left:10px; width:580px; top:504px;">Back side option 2</p>
  <section class="card card--white card--back-two" aria-label="Back side option 2">
    <p class="company company--centered company--dark">
      <span class="company__name">Kestrafield</span>
      <span class="company__line">Information Technology Solutions</span>
    </p>
    <svg class="card__band" viewBox="0 0 580 20" preserveAspectRatio="none" aria-hidden="true">
      <polygon points="0,0 434,0 428,20 0,20" fill="var(--slate)"/>
      <polygon points="440,0 580,0 580,20 434,20" fill="var(--maroon)"/>
    </svg>
  </section>

  <p class="option-label" style="left:610px; width:580px; top:504px;">Back side option 3</p>
  <section class="card card--maroon card--back-three" aria-label="Back side option 3">
    <p class="company company--centered company--light">
      <span class="company__name">Kestrafield</span>
      <span class="company__line">Information Technology Solutions</span>
    </p>
    <svg class="card__band" viewBox="0 0 580 20" preserveAspectRatio="none" aria-hidden="true">
      <polygon points="0,0 434,0 428,20 0,20" fill="var(--paper)"/>
      <polygon points="440,0 580,0 580,20 434,20" fill="var(--slate)"/>
    </svg>
  </section>

</body>
</html>
```